Home Health Agency Marketing Portfolio Booklet

We need a 4 page plus cover (total of 8 pages including front and back cover) design of a Home health Agency Marketing Booklet.
We specialize in taking care of homebound senior patients who needs specialize nursing and medical services in the comfort of their homes. We would like to see a design showing the caring and compassionate nature of our agency. The design should show a nice clean modern layout with nice font selection. Attached is a copy of our logo that needs to be use in the brochure. The colors of the logo should be use in the design of the brochure.
The design will consist of the Front and back cover, inside pages of the cover will be blank but there will be folded pockets that will need some design/color. The inside 4 pages will be full cover, double sided and will have all the information of the company.
The Marketing booklet will be 9"x 12".

```html
<!DOCTYPE html>
<html lang="en">
<head>
<meta charset="utf-8">
<title>Brightwell Home Care – Marketing Booklet</title>
<link rel="stylesheet" href="https://fonts.googleapis.com/css2?family=Montserrat:wght@400;500;600;700;800&family=Roboto:wght@700&display=swap">
<style>
:root{
  --orange:#f39a2c;
  --blue:#0e9ad9;
  --blue-deep:#0a86c6;
  --ink:#2b2b2b;
  --stage:#c9cacb;
  --white:#ffffff;
  --photo-warm:#c9b9a6;
  --photo-cool:#b8ccd6;
  --photo-pale:#e9ecee;
}
*{margin:0;padding:0;box-sizing:border-box}
html,body{width:1200px;height:2580px;overflow:hidden}
body{background:var(--stage);font-family:"Montserrat",sans-serif;color:var(--ink);position:relative}
.spread{position:absolute;left:68px;width:1078px;height:719px;background:var(--white)}
.spread--cover{top:46px}
.spread--inner-a{top:1046px}
.spread--inner-b{top:1813px}
.page{position:absolute;top:0;width:539px;height:719px;overflow:hidden}
.page--left{left:0}
.page--right{left:539px;border-left:1px solid #d4d4d4}
.abs{position:absolute}
.shape-layer{position:absolute;left:0;top:0}

/* Brand wordmark */
.brand{display:flex;align-items:center;gap:10px}
.brand__dot{width:34px;height:34px;border-radius:50%;background:var(--blue);flex:none}
.brand__name{color:var(--orange);font-weight:700;line-height:1.02;letter-spacing:.5px;text-transform:uppercase}

/* Back cover */
.back-brand{left:0;width:539px;top:284px;justify-content:center}
.back-brand .brand__name{font-size:27px}
.info-title{left:0;width:539px;top:395px;text-align:center;color:var(--blue);font-size:15px;font-weight:500;letter-spacing:.3px}
.contact{left:0;width:539px;text-align:center;font-size:7px;color:var(--ink)}
.contact__icon{display:block;margin:0 auto 3px;width:11px;height:11px}
.contact--strong{font-weight:700}

/* Front cover */
.front-brand{left:333px;top:14px;width:177px;height:78px;background:var(--white);justify-content:center;gap:7px}
.front-brand .brand__dot{width:22px;height:22px}
.front-brand .brand__name{font-size:16px}
.tagline{left:0;width:539px;top:606px;text-align:center;color:var(--white)}
.tagline__small{font-size:17px;font-weight:700;letter-spacing:.2px}
.tagline__big{font-size:41px;font-weight:800;line-height:1.05;letter-spacing:.5px}

/* Body text */
.copy{font-size:7.4px;line-height:10px;color:var(--ink)}
.copy p+p{margin-top:10px}
.bullets{list-style:none;font-size:7.4px;line-height:10.5px}
.bullets li{position:relative;padding-left:9px}
.bullets li::before{content:"";position:absolute;left:1px;top:4px;width:3px;height:3px;border-radius:50%;background:var(--ink)}
.bullets--orange li::before{background:var(--orange)}

.section-title{font-size:19px;font-weight:500;color:var(--orange);letter-spacing:.5px;text-transform:uppercase}
.section-title--dark{color:var(--ink);font-size:20px}
.section-title--white{color:var(--white)}

.pill{display:inline-block;background:var(--orange);color:var(--white);font-size:12px;font-weight:500;letter-spacing:.6px;padding:1px 8px;border-radius:0 9px 9px 0;text-transform:uppercase}
.service-pill{display:inline-block;background:var(--blue);color:var(--white);font-family:"Roboto",sans-serif;font-weight:700;font-size:12.5px;letter-spacing:.4px;padding:1px 7px;border-radius:0 9px 9px 0}

.photo{position:absolute}
.about-box{left:323px;top:95px;width:200px;height:312px;background:linear-gradient(180deg,rgba(255,255,255,.95) 60%,rgba(243,154,44,.55) 100%);padding:14px 4px 0 6px}

/* Pocket */
.pocket{position:absolute;left:36px;top:764px}
</style>
</head>
<body>

<!-- Cover spread -->
<section class="spread spread--cover">
  <div class="page page--left back-cover">
    <svg class="shape-layer" width="539" height="719" viewBox="0 0 539 719">
      <rect width="539" height="290" fill="var(--orange)"/>
      <rect y="537" width="539" height="182" fill="var(--blue)"/>
      <path fill="var(--white)" d="M269,255 C245,205 175,195 140,228 C110,255 110,290 120,289 L120,537 C160,585 225,605 260,609 C300,600 360,575 392,537 L392,289 C405,290 410,250 385,228 C350,198 295,205 269,255 Z"/>
    </svg>
    <div class="abs brand back-brand"><span class="brand__dot"></span><span class="brand__name">Brightwell<br>Home Care</span></div>
    <div class="abs info-title">FOR MORE INFORMATION</div>
    <div class="abs contact" style="top:423px">
      <svg class="contact__icon" viewBox="0 0 12 12"><circle cx="6" cy="6" r="6" fill="var(--orange)"/><path d="M6 2.6a2 2 0 0 0-2 2c0 1.5 2 4 2 4s2-2.5 2-4a2 2 0 0 0-2-2z" fill="#fff"/></svg>
      1200 Harbor Lane, Suite 4, Springfield
    </div>
    <div class="abs contact contact--strong" style="top:449px">
      <svg class="contact__icon" viewBox="0 0 12 12"><circle cx="6" cy="6" r="6" fill="var(--orange)"/><path d="M4 3l1.3 1.3-.7.9a5 5 0 0 0 2.2 2.2l.9-.7L9 8 8 9C5.5 9 3 6.5 3 4z" fill="#fff"/></svg>
      0000 000 000, 0000 000 000
    </div>
    <div class="abs contact" style="top:475px">
      <svg class="contact__icon" viewBox="0 0 12 12"><circle cx="6" cy="6" r="6" fill="var(--orange)"/><rect x="3" y="4" width="6" height="4.2" fill="#fff"/><path d="M3 4l3 2.4L9 4" stroke="var(--orange)" stroke-width=".7" fill="none"/></svg>
      info@brightwellhomecare.com
    </div>
    <div class="abs contact" style="top:501px">
      <svg class="contact__icon" viewBox="0 0 12 12"><circle cx="6" cy="6" r="6" fill="var(--orange)"/><circle cx="6" cy="6" r="3" stroke="#fff" stroke-width=".8" fill="none"/><path d="M3 6h6M6 3v6" stroke="#fff" stroke-width=".6"/></svg>
      brightwellhomecare.com
    </div>
  </div>

  <div class="page page--right front-cover">
    <svg class="shape-layer" width="539" height="719" viewBox="0 0 539 719">
      <defs>
        <linearGradient id="coverPhoto" x1="0" y1="0" x2="1" y2="1">
          <stop offset="0" stop-color="#e8ecec"/>
          <stop offset=".45" stop-color="#5fb3c4"/>
          <stop offset="1" stop-color="#b9b2a8"/>
        </linearGradient>
      </defs>
      <rect width="539" height="719" fill="var(--blue)"/>
      <path fill="var(--orange)" d="M0,485 Q250,575 539,470 V512 Q300,620 0,537 Z"/>
      <path role="img" aria-label="Photo: a nurse in blue scrubs pushing a senior woman in a wheelchair at home" fill="url(#coverPhoto)" d="M0,0 H539 V470 Q250,575 0,488 Z"/>
    </svg>
    <div class="abs brand front-brand"><span class="brand__dot"></span><span class="brand__name">Brightwell<br>Home Care</span></div>
    <div class="abs tagline">
      <div class="tagline__small">YOUR HOME IS NOW A</div>
      <div class="tagline__big">THERAPY CENTER</div>
      <div class="tagline__small">WITH US BY YOUR SIDE.</div>
    </div>
  </div>
</section>

<!-- Pocket flap -->
<svg class="pocket" width="574" height="244" viewBox="0 0 574 244">
  <path fill="var(--blue)" stroke="#3a3a3a" stroke-width=".8" d="M32,1 H571 L552,215 Q548,240 525,240 H10 Q2,238 2,230 V14 Q2,8 8,7 L32,1 Z"/>
  <path d="M32,1 V240" stroke="#3a3a3a" stroke-width=".6"/>
</svg>

<!-- Inner spread A -->
<section class="spread spread--inner-a">
  <div class="page page--left">
    <div class="photo" role="img" aria-label="Faded photo of a hospital room with an IV stand and bed" style="left:0;top:0;width:539px;height:719px;background:linear-gradient(90deg,#fff 0%,#fff 42%,#8fd0f0 62%,#2aa3e2 85%,#1894d8 100%)"></div>

    <h2 class="abs section-title" style="left:100px;top:55px">Our Purpose</h2>
    <div class="abs copy" style="left:46px;top:95px;width:258px">
      <p>Our nurses and therapists bring skilled, compassionate care to patients who are homebound. Every visit follows a plan shaped with the family and the physician, so recovery happens safely in familiar surroundings. We listen first, explain each step clearly and adjust care as needs change. Our team is licensed, insured and trained to support seniors with chronic illness, mobility limits and recovery after a hospital stay, always treating every home with patience, dignity and genuine respect.</p>
    </div>
    <ul class="abs bullets" style="left:46px;top:184px;width:220px">
      <li>Skilled nursing visits at home</li>
      <li>Medication management</li>
      <li>Physical and occupational therapy</li>
      <li>Wound care and monitoring</li>
      <li>Family education</li>
      <li>Around-the-clock support line</li>
    </ul>

    <h2 class="abs section-title" style="left:100px;top:306px">Our Goals</h2>
    <div class="abs copy" style="left:46px;top:344px;width:258px">
      <p>Our nurses and therapists bring skilled, compassionate care to patients who are homebound. Every visit follows a plan shaped with the family and the physician, so recovery happens safely in familiar surroundings. We listen first, explain each step clearly and adjust care as needs change. Our team is licensed, insured and trained to support seniors with chronic illness, mobility limits and recovery after a hospital stay, always treating every home with patience, dignity and genuine respect.</p>
      <p>We coordinate with doctors, pharmacies and family members so that every patient receives consistent, well documented care. Our coordinators answer calls day and night and arrange visits that fit the household routine.</p>
    </div>

    <h2 class="abs section-title" style="left:100px;top:512px">Our Objectives</h2>
    <div class="abs copy" style="left:46px;top:551px;width:258px">
      <p>Our nurses and therapists bring skilled, compassionate care to patients who are homebound. Every visit follows a plan shaped with the family and the physician, so recovery happens safely in familiar surroundings. We listen first, explain each step clearly and adjust care as needs change. Our team is licensed, insured and trained to support seniors with chronic illness, mobility limits and recovery after a hospital stay, always treating every home with patience, dignity and genuine respect.</p>
      <p>We coordinate with doctors, pharmacies and family members so that every patient receives consistent, well documented care. Our coordinators answer calls day and night and arrange visits that fit the household routine.</p>
    </div>
  </div>

  <div class="page page--right">
    <svg class="shape-layer" width="539" height="719" viewBox="0 0 539 719">
      <defs>
        <linearGradient id="aboutPhoto" x1="0" y1="0" x2="1" y2="0">
          <stop offset="0" stop-color="#b7aea4"/>
          <stop offset=".55" stop-color="#d9d7d3"/>
          <stop offset="1" stop-color="#eceeee"/>
        </linearGradient>
      </defs>
      <path fill="var(--blue)" d="M0,300 Q120,395 330,405 L539,372 V380 L330,412 Q100,408 0,306 Z"/>
      <path fill="var(--orange)" d="M0,278 Q120,375 330,388 L539,356 V374 L330,404 Q110,396 0,300 Z"/>
      <path role="img" aria-label="Photo: a doctor with a clipboard talking with a senior man on a sofa" fill="url(#aboutPhoto)" d="M0,0 H539 V356 L330,388 Q120,375 0,278 Z"/>
    </svg>
    <h2 class="abs section-title section-title--dark" style="left:375px;top:58px">About Us</h2>
    <div class="abs about-box copy">
      <p>Our nurses and therapists bring skilled, compassionate care to patients who are homebound. Every visit follows a plan shaped with the family and the physician, so recovery happens safely in familiar surroundings. We listen first, explain each step clearly and adjust care as needs change. Our team is licensed, insured and trained to support seniors with chronic illness, mobility limits and recovery after a hospital stay, always treating every home with patience, dignity and genuine respect.</p>
      <p>We coordinate with doctors, pharmacies and family members so that every patient receives consistent, well documented care. Our coordinators answer calls day and night and arrange visits that fit the household routine.</p>
      <p>Our nurses and therapists bring skilled, compassionate care to patients who are homebound. Every visit follows a plan shaped with the family and the physician, so recovery happens safely in familiar surroundings. We listen first, explain each step clearly and adjust care as needs change. Our team is licensed, insured and trained to support seniors with chronic illness, mobility limits and recovery after a hospital stay, always treating every home with patience, dignity and genuine respect.</p>
    </div>

    <h2 class="abs section-title section-title--dark" style="left:27px;top:395px">What We Offer</h2>
    <span class="abs pill" style="left:20px;top:423px">Pediatric Care</span>
    <ul class="abs bullets bullets--orange" style="left:26px;top:448px;width:190px">
      <li>Well-child checks at home</li>
      <li>Feeding support</li>
      <li>Therapy for developmental needs</li>
      <li>Respiratory care and monitoring</li>
      <li>Parent coaching</li>
      <li>Medication support for children</li>
    </ul>
    <div class="photo" role="img" aria-label="Photo: a pediatric nurse listening to a young girl's heartbeat with a stethoscope" style="left:0;top:579px;width:231px;height:140px;background:linear-gradient(135deg,#e6d3c0,#cdb8a6 50%,#9fb2c6)"></div>
    <div class="photo" role="img" aria-label="Photo: a masked doctor giving a vaccine to a senior woman" style="left:325px;top:422px;width:214px;height:144px;background:linear-gradient(135deg,#dfe4e6,#a9c3d4 50%,#e2d6c9)"></div>
    <span class="abs pill" style="left:313px;top:574px">Adult Care</span>
    <ul class="abs bullets bullets--orange" style="left:320px;top:598px;width:200px">
      <li>Post-hospital recovery care</li>
      <li>Chronic disease care</li>
      <li>Fall prevention and safety checks</li>
      <li>Personal care assistance</li>
      <li>Companionship</li>
    </ul>
  </div>
</section>

<!-- Inner spread B -->
<section class="spread spread--inner-b">
  <div class="page page--left">
    <svg class="shape-layer" width="539" height="719" viewBox="0 0 539 719">
      <defs>
        <linearGradient id="missionPhoto" x1="0" y1="0" x2="1" y2="1">
          <stop offset="0" stop-color="#5c7a95"/>
          <stop offset=".5" stop-color="#b9a496"/>
          <stop offset="1" stop-color="#4d86b3"/>
        </linearGradient>
      </defs>
      <path fill="var(--blue)" d="M0,382 Q300,388 539,322 V332 Q300,398 0,392 Z"/>
      <path fill="var(--orange)" d="M0,278 Q300,290 539,248 V322 Q300,388 0,382 Z"/>
      <path role="img" aria-label="Photo: a male nurse helping a senior woman in a wheelchair exercise with a dumbbell" fill="url(#missionPhoto)" d="M0,0 H539 V248 Q300,290 0,278 Z"/>
    </svg>
    <h2 class="abs section-title section-title--white" style="left:46px;top:338px">Our Missions &amp; Vision</h2>
    <div class="abs copy" style="left:46px;top:411px;width:442px">
      <p>Our nurses and therapists bring skilled, compassionate care to patients who are homebound. Every visit follows a plan shaped with the family and the physician, so recovery happens safely in familiar surroundings. We listen first, explain each step clearly and adjust care as needs change. Our team is licensed, insured and trained to support seniors with chronic illness, mobility limits and recovery after a hospital stay, always treating every home with patience, dignity and genuine respect.</p>
      <p>We coordinate with doctors, pharmacies and family members so that every patient receives consistent, well documented care. Our coordinators answer calls day and night and arrange visits that fit the household routine.</p>
      <p>Our nurses and therapists bring skilled, compassionate care to patients who are homebound. Every visit follows a plan shaped with the family and the physician, so recovery happens safely in familiar surroundings. We listen first, explain each step clearly and adjust care as needs change. Our team is licensed, insured and trained to support seniors with chronic illness, mobility limits and recovery after a hospital stay, always treating every home with patience, dignity and genuine respect.</p>
    </div>
    <h2 class="abs section-title" style="left:46px;top:581px">Why Are We Brightwell?</h2>
    <div class="abs copy" style="left:46px;top:625px;width:442px">
      <p>Our nurses and therapists bring skilled, compassionate care to patients who are homebound. Every visit follows a plan shaped with the family and the physician, so recovery happens safely in familiar surroundings. We listen first, explain each step clearly and adjust care as needs change. Our team is licensed, insured and trained to support seniors with chronic illness, mobility limits and recovery after a hospital stay, always treating every home with patience, dignity and genuine respect.</p>
    </div>
  </div>

  <div class="page page--right">
    <svg class="shape-layer" width="539" height="719" viewBox="0 0 539 719">
      <path fill="var(--blue)" d="M0,112 Q300,132 539,92 V100 Q300,142 0,122 Z"/>
      <path fill="var(--orange)" d="M0,0 H539 V92 Q300,132 0,112 Z"/>
    </svg>
    <h2 class="abs section-title section-title--white" style="left:60px;top:42px;line-height:24px">Our Home Health Care<br>Services Include:</h2>

    <span class="abs service-pill" style="left:52px;top:137px">In-Home Support Services</span>
    <div class="abs copy" style="left:60px;top:173px;width:192px"><p>Trained aides help with bathing, dressing, meals, light housekeeping and errands, giving patients the support they need to stay independent at home. Each care plan is reviewed by a registered nurse and updated whenever health or routines change. Families receive regular updates and a single point of contact for questions, scheduling and billing, so that care remains simple, steady and reassuring from the very first visit.</p></div>

    <span class="abs service-pill" style="left:282px;top:137px">Private Duty Nursing</span>
    <div class="abs copy" style="left:290px;top:173px;width:192px"><p>Trained aides help with bathing, dressing, meals, light housekeeping and errands, giving patients the support they need to stay independent at home. Each care plan is reviewed by a registered nurse and updated whenever health or routines change. Families receive regular updates and a single point of contact for questions, scheduling and billing, so that care remains simple, steady and reassuring from the very first visit.</p></div>

    <span class="abs service-pill" style="left:52px;top:312px">Family Care Provider</span>
    <div class="abs copy" style="left:60px;top:344px;width:192px"><p>Trained aides help with bathing, dressing, meals, light housekeeping and errands, giving patients the support they need to stay independent at home. Each care plan is reviewed by a registered nurse and updated whenever health or routines change. Families receive regular updates and a single point of contact for questions, scheduling and billing, so that care remains simple, steady and reassuring from the very first visit.</p></div>

    <span class="abs service-pill" style="left:282px;top:312px">Senior Care</span>
    <div class="abs copy" style="left:290px;top:344px;width:192px"><p>Trained aides help with bathing, dressing, meals, light housekeeping and errands, giving patients the support they need to stay independent at home. Each care plan is reviewed by a registered nurse and updated whenever health or routines change. Families receive regular updates and a single point of contact for questions, scheduling and billing, so that care remains simple, steady and reassuring from the very first visit.</p></div>

    <div class="photo" role="img" aria-label="Photo: a white first aid box with a red cross beside medicine bottles and pills" style="left:150px;top:477px;width:389px;height:242px;background:linear-gradient(90deg,rgba(255,255,255,1) 0%,var(--photo-pale) 30%,#dcdfe2 100%)"></div>

    <span class="abs service-pill" style="left:52px;top:487px">Pediatric Home Care</span>
    <div class="abs copy" style="left:60px;top:519px;width:192px"><p>Trained aides help with bathing, dressing, meals, light housekeeping and errands, giving patients the support they need to stay independent at home. Each care plan is reviewed by a registered nurse and updated whenever health or routines change. Families receive regular updates and a single point of contact for questions, scheduling and billing, so that care remains simple, steady and reassuring from the very first visit.</p></div>
  </div>

  <svg class="shape-layer" width="1078" height="719" viewBox="0 0 1078 719" style="pointer-events:none">
    <path fill="var(--blue)" d="M420,719 L539,640 L692,719 Z"/>
    <path fill="var(--orange)" d="M440,719 L539,652 L672,719 Z"/>
    <path d="M539,652 V719" stroke="#d4d4d4" stroke-width="1"/>
  </svg>
</section>

</body>
</html>
```